Need Business Cards for my Business

email address: rkpmarlowhollowworks@vendrimail.com
web address: rkpmarlowhollowworks.net
Slogan: We offer various QVN licenses
Rowland K. Pemberly
Please stick with colors of Company Logo
would like the card to be more of the color example of the logo.
If you need PDF copy of logo email me at the above account.
Creative control rests with you.

Industry/Entity Type

Business

Contact Information for Business Card

I am a minimalist, but would like something to pop and stand out amongst other cards, make it memorable.

Font styles to use
Serif
Decorative
Script

```html
<!DOCTYPE html>
<html lang="en">
<head>
<meta charset="utf-8">
<title>Rowland K. Pemberly — Business Card</title>
<link rel="stylesheet" href="https://fonts.googleapis.com/css2?family=Caladea&family=Bitter:wght@500&display=swap">
<style>
  :root {
    --backdrop: #e4e1dc;
    --card-dark: #0e0c10;
    --card-light: #ffffff;
    --ink-light: #f4f4f4;
    --ink-dark: #111111;
    --rule-dark: #6a6a6a;
  }
  * { margin: 0; padding: 0; box-sizing: border-box; }
  html, body {
    width: 1200px;
    height: 1000px;
    overflow: hidden;
    background: var(--backdrop);
  }
  .canvas {
    position: relative;
    width: 1200px;
    height: 1000px;
  }
  .card {
    position: absolute;
    left: 243px;
    width: 709px;
    height: 405px;
  }
  .card--front {
    top: 84px;
    background: var(--card-dark);
    color: var(--ink-light);
  }
  .card--back {
    top: 526px;
    background: var(--card-light);
    color: var(--ink-dark);
    text-align: center;
  }
  .brand {
    position: absolute;
    top: 148px;
    left: 0;
    width: 100%;
    display: flex;
    align-items: center;
    justify-content: center;
    gap: 22px;
  }
  .brand__dot {
    width: 70px;
    height: 70px;
    border-radius: 50%;
    background: var(--ink-light);
  }
  .brand__name {
    font-family: "Caladea", serif;
    font-size: 42px;
    line-height: 1.1;
    letter-spacing: 1px;
    color: var(--ink-light);
  }
  .slogan {
    position: absolute;
    top: 328px;
    left: 0;
    width: 100%;
    display: flex;
    align-items: center;
    justify-content: center;
    gap: 12px;
    font-family: "Caladea", serif;
    font-size: 16px;
    letter-spacing: 0.4px;
    color: #e8e8e8;
  }
  .slogan__rule {
    width: 92px;
    height: 1px;
  }
  .slogan__rule--left { background: linear-gradient(to right, transparent, var(--rule-dark)); }
  .slogan__rule--right { background: linear-gradient(to left, transparent, var(--rule-dark)); }
  .holder {
    position: absolute;
    top: 132px;
    left: 0;
    width: 100%;
  }
  .holder__name {
    font-family: "Bitter", serif;
    font-weight: 500;
    font-size: 23px;
    letter-spacing: 1.6px;
    text-transform: uppercase;
  }
  .holder__rule {
    width: 58px;
    height: 2px;
    background: var(--ink-dark);
    margin: 8px auto 0;
  }
  .contact {
    list-style: none;
    margin-top: 20px;
    font-family: "Caladea", serif;
    font-size: 16px;
    line-height: 28.5px;
    letter-spacing: 0.3px;
  }
</style>
</head>
<body>
  <main class="canvas">
    <section class="card card--front">
      <div class="brand">
        <span class="brand__dot"></span>
        <span class="brand__name">RKP Marlow Hollow Works</span>
      </div>
      <p class="slogan">
        <span class="slogan__rule slogan__rule--left"></span>
        <span>We offer various QVN licenses</span>
        <span class="slogan__rule slogan__rule--right"></span>
      </p>
    </section>

    <section class="card card--back">
      <div class="holder">
        <h1 class="holder__name">Rowland K. Pemberly</h1>
        <div class="holder__rule"></div>
        <ul class="contact">
          <li>0412 583 906</li>
          <li>rkpmarlowhollowworks@vendrimail.com</li>
          <li>rkpmarlowhollowworks.net</li>
        </ul>
      </div>
    </section>
  </main>
</body>
</html>
```